KWB Staffing Proven Process - Staffing Agency for delivery and website

We're seeking a one-page graphic design for distribution to potential clients and for our website. This design will outline the step-by-step expectations for clients considering our services. This process is known as "The KWB Proven Process."

Step 1: "The Initial Challenge"
Visual: Depict a puzzled project manager.
Description: The project manager encounters a challenge and reaches out to us.
• About YOU
• About KWB
• The Process

Step 2: "KWB Activation"
Visual: Illustrate our response with an employee transforming into a knight with a shovel and hard hat.
Description: We swiftly activate our team to craft a customized solution through our Talent Forge.
• Recruiting
• Filtering
• Keeping YOU informed
• Delivering solutions

Step 3: "Triumphant Resolution"
Visual: Show a relaxed project manager enjoying a stress-free moment with a piña colada on a beach.
Description: The project concludes successfully, with the project manager at ease.
• Follow up!
• Meeting expectations
• Building Relationships

Design Guidelines:
*Maintain a clean and professional layout.
*Integrate our brand's color scheme and logo.
*Incorporate relevant icons or graphics for each step.
*Utilize a legible font with clear headings.

Target Market(s)

Employers

Industry/Entity Type

Construction, Restoration, Industrial

Colors
F0912C
F2A743
F7CA91
FBE8D2
FDF5EE
EE7325
F08F49
F5BC92
FAE3D3
FDF4ED

Requirements
Must have
• KWB Logo,
Nice to have
• Our Niche "Delivering solutions for complex problems"
Should not have
• Please do not include the words STEP 1, STEP 2, or STEP 3.

```html
<!DOCTYPE html>
<html lang="en">
<head>
<meta charset="utf-8">
<title>KWB Proven Process</title>
<link rel="stylesheet" href="https://fonts.googleapis.com/css2?family=Oswald:wght@600;700&family=Poppins:wght@400;600;700;800&display=swap">
<style>
  :root{
    --stage:#dedede;
    --paper:#ffffff;
    --blue:#0577b6;
    --navy:#0f3b6e;
    --orange:#fb7416;
    --orange-soft:#fbd3b4;
    --sky:#86cff6;
    --ink:#1c1c1c;
    --map:#f3f3f3;
    --hex-ring:#e4e4e4;
  }
  *{margin:0;padding:0;box-sizing:border-box}
  html,body{width:1200px;height:2162px;overflow:hidden}
  body{background:var(--stage);font-family:"Poppins",sans-serif;color:var(--ink);position:relative}

  .sheet{position:absolute;background:var(--paper);box-shadow:0 4px 14px rgba(0,0,0,.18);overflow:hidden}
  .sheet--portrait{left:248px;top:133px;width:704px;height:912px}
  .sheet--landscape{left:122px;top:1200px;width:956px;height:737px}

  .world-map{position:absolute;background:radial-gradient(ellipse at center,var(--map) 0%,rgba(243,243,243,0) 70%)}
  .sheet--portrait .world-map{left:0;top:260px;width:704px;height:480px}
  .sheet--landscape .world-map{left:60px;top:160px;width:840px;height:440px}

  .brand-mark{position:absolute;display:flex;align-items:center;justify-content:center;font-family:"Poppins",sans-serif;font-weight:800;color:var(--orange);letter-spacing:2px;white-space:nowrap}
  .sheet--portrait .brand-mark{left:263px;top:35px;width:178px;height:122px;font-size:72px}
  .sheet--landscape .brand-mark{left:45px;top:34px;width:189px;height:124px;font-size:68px}

  .title-band{position:absolute;color:#fff;font-family:"Oswald",sans-serif;font-weight:700;line-height:1;white-space:nowrap}
  .title-band--full{left:0;top:181px;width:704px;height:77px;background:var(--blue);display:flex;align-items:center;justify-content:center;font-size:60px;letter-spacing:-0.5px}
  .title-band--full span{display:inline-block;transform:scaleY(1.12)}
  .title-band--slanted{left:250px;top:30px;width:661px;height:128px}
  .title-band--slanted svg{position:absolute;left:0;top:0}
  .title-band--slanted span{position:absolute;right:22px;top:0;height:128px;display:flex;align-items:center;font-size:62px;letter-spacing:-0.5px;transform:scaleY(1.2)}

  .step-row{position:absolute;left:39px;width:660px;height:105px}
  .step-row svg{position:absolute;left:0;top:0}
  .step-tag{position:absolute;left:0;top:0;width:108px;height:105px;display:flex;align-items:center;justify-content:center;text-align:center;color:#fff;font-weight:800;font-size:20px;line-height:20px}
  .step-name{position:absolute;left:133px;top:0;height:105px;display:flex;align-items:center;color:#fff;font-weight:700;font-size:17px;line-height:22px}
  .step-icon{position:absolute;left:315px;top:14px;width:86px;height:78px;border-radius:12px}
  .step-copy{position:absolute;left:427px;width:230px;font-size:16.5px;line-height:19.5px;color:var(--ink)}

  .tagline{position:absolute;background:var(--orange);color:#fff;font-weight:700;display:flex;align-items:center;justify-content:center;white-space:nowrap}
  .sheet--portrait .tagline{left:37px;top:753px;width:629px;height:35px;font-size:25px}
  .sheet--landscape .tagline{left:43px;top:623px;width:870px;height:47px;font-size:34px}

  .site-url{position:absolute;left:0;width:100%;text-align:center;font-weight:400;letter-spacing:.22em}
  .sheet--portrait .site-url{top:810px;font-size:37px}
  .sheet--landscape .site-url{top:677px;font-size:30px}

  .connector{position:absolute;left:0;top:0}
  .step-card{position:absolute;top:207px;width:210px;height:277px;background:#fff;border-radius:8px;box-shadow:0 1px 5px rgba(0,0,0,.22)}
  .step-card__head{position:absolute;left:11px;top:14px;width:188px;height:63px;border-radius:6px 6px 0 0;color:#fff;font-weight:700;font-size:37px;display:flex;align-items:center;justify-content:center;white-space:nowrap}
  .step-card__art{position:absolute;left:11px;top:77px;width:188px;height:186px;border-radius:0 0 6px 6px}
  .step-card--one{left:65px}.step-card--two{left:376px}.step-card--three{left:685px}
  .step-caption{position:absolute;top:525px;width:290px;text-align:center}
  .step-caption h3{font-weight:700;font-size:19.5px;line-height:24px;white-space:nowrap}
  .step-caption p{font-size:12.3px;line-height:14.6px;margin:4px auto 0;width:225px}
  .caption--one{left:25px}.caption--two{left:335px}.caption--three{left:645px}
  .is-blue{color:var(--blue)}.is-orange{color:var(--orange)}
  .bg-blue{background:var(--blue)}.bg-orange{background:var(--orange)}
</style>
</head>
<body>

<section class="sheet sheet--portrait">
  <div class="world-map" role="img" aria-label="Faint world map backdrop"></div>
  <div class="brand-mark">KWB</div>
  <h1 class="title-band title-band--full"><span>KWB PROVEN PROCESS</span></h1>

  <div class="step-row" style="top:308px">
    <svg width="300" height="105" viewBox="0 0 300 105">
      <polygon points="60,5 274,5 296,52 274,100 60,100" fill="var(--orange)"/>
      <polygon points="2,52 28,4 80,4 106,52 80,100 28,100" fill="#fff" stroke="var(--orange)" stroke-width="3"/>
      <polygon points="14,52 34,17 74,17 94,52 74,87 34,87" fill="var(--orange)" stroke="var(--hex-ring)" stroke-width="4"/>
    </svg>
    <div class="step-tag">STEP<br>01</div>
    <div class="step-name">THE INITIAL<br>CHALLENGE</div>
    <div class="step-icon bg-orange" role="img" aria-label="Icon of a manager beside a gear"></div>
    <p class="step-copy" style="top:12px">The project manager encounters a challenge and reaches out to us through our Talent Forge.</p>
  </div>

  <div class="step-row" style="top:460px">
    <svg width="300" height="105" viewBox="0 0 300 105">
      <polygon points="60,5 274,5 296,52 274,100 60,100" fill="var(--blue)"/>
      <polygon points="2,52 28,4 80,4 106,52 80,100 28,100" fill="#fff" stroke="var(--blue)" stroke-width="3"/>
      <polygon points="14,52 34,17 74,17 94,52 74,87 34,87" fill="var(--blue)" stroke="var(--hex-ring)" stroke-width="4"/>
    </svg>
    <div class="step-tag">STEP<br>02</div>
    <div class="step-name">KWB<br>ACTIVATION</div>
    <div class="step-icon" role="img" aria-label="Icon of an armoured knight with a tool" style="background:linear-gradient(135deg,var(--orange),var(--blue))"></div>
    <p class="step-copy" style="top:24px;width:210px">We swiftly activate our team to craft a customized solution.</p>
  </div>

  <div class="step-row" style="top:612px">
    <svg width="300" height="105" viewBox="0 0 300 105">
      <polygon points="60,5 274,5 296,52 274,100 60,100" fill="var(--orange)"/>
      <polygon points="2,52 28,4 80,4 106,52 80,100 28,100" fill="#fff" stroke="var(--orange)" stroke-width="3"/>
      <polygon points="14,52 34,17 74,17 94,52 74,87 34,87" fill="var(--orange)" stroke="var(--hex-ring)" stroke-width="4"/>
    </svg>
    <div class="step-tag">STEP<br>03</div>
    <div class="step-name">TRIUMPHANT<br>RESOLUTION</div>
    <div class="step-icon" role="img" aria-label="Icon of a person relaxing under a beach umbrella" style="background:linear-gradient(135deg,var(--orange),var(--blue))"></div>
    <p class="step-copy" style="top:22px;width:220px">The project concludes successfully, with the project manager at ease.</p>
  </div>

  <div class="tagline">Delivering solutions for complex problems</div>
  <div class="site-url">www.pskwb.com</div>
</section>

<section class="sheet sheet--landscape">
  <div class="world-map" role="img" aria-label="Faint world map backdrop"></div>
  <div class="brand-mark">KWB</div>
  <h1 class="title-band title-band--slanted">
    <svg width="661" height="128" viewBox="0 0 661 128">
      <polygon points="0,0 14,0 84,128 70,128" fill="var(--orange)"/>
      <polygon points="14,0 661,0 661,128 84,128" fill="var(--blue)"/>
    </svg>
    <span>KWB PROVEN PROCESS</span>
  </h1>

  <svg class="connector" width="956" height="620" viewBox="0 0 956 620">
    <path d="M48 264 V480 Q48 501 69 501 H270 Q291 501 291 480 V285 Q291 265 311 265 H338 Q358 265 358 285 V480 Q358 501 379 501 H580 Q601 501 601 480 V285 Q601 265 621 265 H650 Q670 265 670 285 V480 Q670 501 691 501 H890 Q911 501 911 480 V264" fill="none" stroke="var(--navy)" stroke-width="1.6"/>
    <circle cx="48" cy="264" r="5" fill="var(--orange)"/>
    <circle cx="326" cy="265" r="5" fill="var(--orange)"/>
    <circle cx="634" cy="265" r="5" fill="var(--orange)"/>
    <circle cx="913" cy="264" r="5" fill="var(--orange)"/>
  </svg>

  <article class="step-card step-card--one">
    <div class="step-card__head bg-blue">STEP 01</div>
    <div class="step-card__art" role="img" aria-label="Illustration of a construction manager in a hard hat holding a checklist" style="background:linear-gradient(160deg,var(--orange-soft),#5a89b4)"></div>
  </article>
  <article class="step-card step-card--two">
    <div class="step-card__head bg-orange">STEP 02</div>
    <div class="step-card__art" role="img" aria-label="Illustration of a knight on a rearing horse holding a shovel" style="background:var(--sky)"></div>
  </article>
  <article class="step-card step-card--three">
    <div class="step-card__head bg-blue">STEP 03</div>
    <div class="step-card__art" role="img" aria-label="Illustration of a relaxed traveller under a beach umbrella with a suitcase" style="background:linear-gradient(180deg,var(--orange-soft),#f7b98f)"></div>
  </article>

  <div class="step-caption caption--one">
    <h3 class="is-blue">THE INITIAL CHALLENGE</h3>
    <p>The project manager encounters a challenge and reaches out to us through our Talent Forge.</p>
  </div>
  <div class="step-caption caption--two">
    <h3 class="is-orange">KWB ACTIVATION</h3>
    <p>We swiftly activate our team to craft a customized solution.</p>
  </div>
  <div class="step-caption caption--three">
    <h3 class="is-blue">TRIUMPHANT RESOLUTION</h3>
    <p>The project concludes successfully, with the project manager at ease.</p>
  </div>

  <div class="tagline">Delivering solutions for complex problems</div>
  <div class="site-url">www.pskwb.com</div>
</section>

</body>
</html>
```